FLOUR BAG DESIGN

• Bag dimensions: H=280 mm, A=105 mm, B=65 mm (look at the picture »dimensions«)
• Bag will be used for different types of flour (wheat flour, corn flour, buckwheat flour, etc.) and porridge (buckwheat, millet, etc. ) so we are looking for universal design that will suit to all of them. Please have in mind that somewhere on the front side (AxH) there needs to be some space for the name of the flour/porridge.
• I also uploaded design of an existing bag just in case you want to see it. Design on the bag represents the mill where our business started. We could say that existing bag is very traditional, we are looking for a little bit more modern style bag but still want to emphasize the link to our tradition.

I forgot to select "10 days " when desribing the label desing I need, before posting the project

• • We would like to integrate our logo (look at the picture »logo«) and text which is also present on the current bag. Front side AxH: Brezarjev Mlin (name of the company), Fužina – Zagradec (name of the village), Meljemo že od 1754 (meaning Flour milling since 1682). On the right side: same as on the picture »current bag (dimensions BxH)«.

```html
<!DOCTYPE html>
<html lang="sl">
<head>
<meta charset="utf-8">
<title>Brezarjev Mlin – flour bag labels</title>
<link href="https://fonts.googleapis.com/css2?family=Arimo:ital,wght@0,400;0,700;1,400&display=swap" rel="stylesheet">
<style>
  :root {
    --brown: #6b4a2b;
    --brown-dark: #4f3620;
    --tan: #b08c68;
    --sun: #f7dc7a;
    --paper: #ffffff;
    --wheat: #6e4526;
    --corn: #4a5650;
    --buckwheat: #8c7747;
    --millet: #4f6a3c;
  }
  html, body { margin: 0; padding: 0; overflow: hidden; background: var(--paper); }
  .label-sheet {
    position: relative; width: 1200px; height: 800px; overflow: hidden;
    background: var(--paper); font-family: "Arimo", Arial, sans-serif; color: var(--brown);
    box-sizing: border-box; border: 1px solid var(--brown);
  }
  .bag-front {
    position: absolute; top: 0; width: 298px; height: 800px; overflow: hidden;
    border-right: 2px solid var(--brown); box-sizing: border-box;
  }
  .bag-front:last-child { border-right: none; }
  .bag-front--wheat { left: 0; --band: var(--wheat); }
  .bag-front--corn { left: 298px; --band: var(--corn); }
  .bag-front--buckwheat { left: 596px; --band: var(--buckwheat); }
  .bag-front--millet { left: 894px; --band: var(--millet); }

  .brand-mark {
    position: absolute; top: 72px; left: 50%; width: 72px; height: 72px; margin-left: -36px;
    border-radius: 50%; background: var(--brown);
  }
  .brand-name {
    position: absolute; top: 166px; left: 0; right: 0; text-align: center;
    font-size: 29px; font-weight: 400; color: var(--brown);
  }
  .product-ribbon { position: absolute; top: 250px; left: 32px; width: 256px; height: 62px; }
  .product-ribbon svg { position: absolute; inset: 0; }
  .product-ribbon .band { fill: var(--band); }
  .product-name {
    position: absolute; top: 12px; left: 26px; right: 26px; text-align: center;
    font-weight: 700; font-size: 20px; color: #fff; letter-spacing: 0.5px;
    transform: rotate(1.5deg); text-shadow: 0 1px 1px rgba(0,0,0,.35); white-space: nowrap;
  }
  .product-name--long { font-size: 17px; letter-spacing: 0.2px; }
  .mill-scene {
    position: absolute; top: 304px; left: 40px; width: 218px; height: 140px;
    border-radius: 45% 45% 40% 40% / 50% 50% 40% 40%;
    background: radial-gradient(ellipse at 50% 55%, #d9bf9c 0%, #ead9c1 55%, rgba(255,255,255,0) 78%);
  }
  .tagline {
    position: absolute; top: 452px; left: 0; right: 0; text-align: center;
    font-size: 21px; color: var(--brown); transform: rotate(-2deg);
  }
  .footer-wave { position: absolute; left: 0; top: 540px; width: 298px; height: 260px; }
  .sun-glow { fill: url(#sun); }
  .contact {
    position: absolute; top: 638px; left: 0; right: 0; text-align: center; color: var(--brown-dark);
  }
  .contact-company { font-weight: 700; font-size: 17px; margin: 0; }
  .contact-line { font-weight: 700; font-size: 11.5px; margin: 2px 0 0; }
  .contact-phones { margin-top: 20px; }
  .contact-phone { font-style: italic; font-size: 11.5px; margin: 0; line-height: 14px; }
  .contact-web { font-style: italic; font-size: 11.5px; margin: 18px 0 0; }
</style>
</head>
<body>
<svg width="0" height="0" style="position:absolute">
  <defs>
    <radialGradient id="sun" cx="50%" cy="0%" r="95%">
      <stop offset="0%" stop-color="#f7d66a"/>
      <stop offset="45%" stop-color="#fbeaa8"/>
      <stop offset="100%" stop-color="#ffffff"/>
    </radialGradient>
  </defs>
</svg>
<main class="label-sheet">

  <section class="bag-front bag-front--wheat">
    <div class="brand-mark"></div>
    <div class="brand-name">Brezarjev mlin</div>
    <div class="product-ribbon">
      <svg viewBox="0 0 256 62"><polygon class="band" points="0,22 34,22 34,52 0,52 12,37" opacity=".85"/><polygon class="band" points="256,16 222,16 222,46 256,46 244,31" opacity=".85"/><polygon class="band" points="24,8 232,4 232,40 24,44"/><polygon points="24,44 34,52 34,44" fill="#000" opacity=".35"/><polygon points="232,40 222,46 222,40" fill="#000" opacity=".35"/></svg>
      <div class="product-name">WHEAT FLOUR</div>
    </div>
    <div class="mill-scene" role="img" aria-label="Sepia drawing of the old mill buildings by the stream"></div>
    <div class="tagline">Meljemo že od 1754</div>
    <svg class="footer-wave" viewBox="0 0 298 260"><path class="sun-glow" d="M0,80 C70,80 110,60 149,30 C188,60 228,80 298,80 L298,250 L0,250 Z"/><path d="M0,62 C70,62 110,42 149,14 C188,42 228,62 298,62 L298,72 C228,72 188,52 149,24 C110,52 70,72 0,72 Z" fill="var(--tan)"/><path d="M0,80 C70,80 110,60 149,30 C188,60 228,80 298,80" fill="none" stroke="var(--brown)" stroke-width="3"/><path d="M0,88 C70,88 110,68 149,38 C188,68 228,88 298,88" fill="none" stroke="var(--brown)" stroke-width="1.5"/><path d="M0,258 C50,240 100,236 149,246 C198,236 248,240 298,258" fill="none" stroke="var(--brown)" stroke-width="2.5"/></svg>
    <div class="contact">
      <p class="contact-company">Brezarjev Mlin</p>
      <p class="contact-line">Tomaž Kralj s.p.</p>
      <p class="contact-line">Potok 18, 1296 Šentvid</p>
      <div class="contact-phones"><p class="contact-phone">T: 01 555 20 40</p><p class="contact-phone">M: 040 123 456</p></div>
      <p class="contact-web">www.brezarjev-mlin.si</p>
    </div>
  </section>

  <section class="bag-front bag-front--corn">
    <div class="brand-mark"></div>
    <div class="brand-name">Brezarjev mlin</div>
    <div class="product-ribbon">
      <svg viewBox="0 0 256 62"><polygon class="band" points="0,22 34,22 34,52 0,52 12,37" opacity=".85"/><polygon class="band" points="256,16 222,16 222,46 256,46 244,31" opacity=".85"/><polygon class="band" points="24,8 232,4 232,40 24,44"/><polygon points="24,44 34,52 34,44" fill="#000" opacity=".35"/><polygon points="232,40 222,46 222,40" fill="#000" opacity=".35"/></svg>
      <div class="product-name">CORN FLOUR</div>
    </div>
    <div class="mill-scene" role="img" aria-label="Sepia drawing of the old mill buildings by the stream"></div>
    <div class="tagline">Meljemo že od 1754</div>
    <svg class="footer-wave" viewBox="0 0 298 260"><path class="sun-glow" d="M0,80 C70,80 110,60 149,30 C188,60 228,80 298,80 L298,250 L0,250 Z"/><path d="M0,62 C70,62 110,42 149,14 C188,42 228,62 298,62 L298,72 C228,72 188,52 149,24 C110,52 70,72 0,72 Z" fill="var(--tan)"/><path d="M0,80 C70,80 110,60 149,30 C188,60 228,80 298,80" fill="none" stroke="var(--brown)" stroke-width="3"/><path d="M0,88 C70,88 110,68 149,38 C188,68 228,88 298,88" fill="none" stroke="var(--brown)" stroke-width="1.5"/><path d="M0,258 C50,240 100,236 149,246 C198,236 248,240 298,258" fill="none" stroke="var(--brown)" stroke-width="2.5"/></svg>
    <div class="contact">
      <p class="contact-company">Brezarjev Mlin</p>
      <p class="contact-line">Tomaž Kralj s.p.</p>
      <p class="contact-line">Potok 18, 1296 Šentvid</p>
      <div class="contact-phones"><p class="contact-phone">T: 01 555 20 40</p><p class="contact-phone">M: 040 123 456</p></div>
      <p class="contact-web">www.brezarjev-mlin.si</p>
    </div>
  </section>

  <section class="bag-front bag-front--buckwheat">
    <div class="brand-mark"></div>
    <div class="brand-name">Brezarjev mlin</div>
    <div class="product-ribbon">
      <svg viewBox="0 0 256 62"><polygon class="band" points="0,22 34,22 34,52 0,52 12,37" opacity=".85"/><polygon class="band" points="256,16 222,16 222,46 256,46 244,31" opacity=".85"/><polygon class="band" points="24,8 232,4 232,40 24,44"/><polygon points="24,44 34,52 34,44" fill="#000" opacity=".35"/><polygon points="232,40 222,46 222,40" fill="#000" opacity=".35"/></svg>
      <div class="product-name product-name--long">BUCKWHEAT FLOUR</div>
    </div>
    <div class="mill-scene" role="img" aria-label="Sepia drawing of the old mill buildings by the stream"></div>
    <div class="tagline">Meljemo že od 1754</div>
    <svg class="footer-wave" viewBox="0 0 298 260"><path class="sun-glow" d="M0,80 C70,80 110,60 149,30 C188,60 228,80 298,80 L298,250 L0,250 Z"/><path d="M0,62 C70,62 110,42 149,14 C188,42 228,62 298,62 L298,72 C228,72 188,52 149,24 C110,52 70,72 0,72 Z" fill="var(--tan)"/><path d="M0,80 C70,80 110,60 149,30 C188,60 228,80 298,80" fill="none" stroke="var(--brown)" stroke-width="3"/><path d="M0,88 C70,88 110,68 149,38 C188,68 228,88 298,88" fill="none" stroke="var(--brown)" stroke-width="1.5"/><path d="M0,258 C50,240 100,236 149,246 C198,236 248,240 298,258" fill="none" stroke="var(--brown)" stroke-width="2.5"/></svg>
    <div class="contact">
      <p class="contact-company">Brezarjev Mlin</p>
      <p class="contact-line">Tomaž Kralj s.p.</p>
      <p class="contact-line">Potok 18, 1296 Šentvid</p>
      <div class="contact-phones"><p class="contact-phone">T: 01 555 20 40</p><p class="contact-phone">M: 040 123 456</p></div>
      <p class="contact-web">www.brezarjev-mlin.si</p>
    </div>
  </section>

  <section class="bag-front bag-front--millet">
    <div class="brand-mark"></div>
    <div class="brand-name">Brezarjev mlin</div>
    <div class="product-ribbon">
      <svg viewBox="0 0 256 62"><polygon class="band" points="0,22 34,22 34,52 0,52 12,37" opacity=".85"/><polygon class="band" points="256,16 222,16 222,46 256,46 244,31" opacity=".85"/><polygon class="band" points="24,8 232,4 232,40 24,44"/><polygon points="24,44 34,52 34,44" fill="#000" opacity=".35"/><polygon points="232,40 222,46 222,40" fill="#000" opacity=".35"/></svg>
      <div class="product-name product-name--long">MILLET PORRIDGE</div>
    </div>
    <div class="mill-scene" role="img" aria-label="Sepia drawing of the old mill buildings by the stream"></div>
    <div class="tagline">Meljemo že od 1754</div>
    <svg class="footer-wave" viewBox="0 0 298 260"><path class="sun-glow" d="M0,80 C70,80 110,60 149,30 C188,60 228,80 298,80 L298,250 L0,250 Z"/><path d="M0,62 C70,62 110,42 149,14 C188,42 228,62 298,62 L298,72 C228,72 188,52 149,24 C110,52 70,72 0,72 Z" fill="var(--tan)"/><path d="M0,80 C70,80 110,60 149,30 C188,60 228,80 298,80" fill="none" stroke="var(--brown)" stroke-width="3"/><path d="M0,88 C70,88 110,68 149,38 C188,68 228,88 298,88" fill="none" stroke="var(--brown)" stroke-width="1.5"/><path d="M0,258 C50,240 100,236 149,246 C198,236 248,240 298,258" fill="none" stroke="var(--brown)" stroke-width="2.5"/></svg>
    <div class="contact">
      <p class="contact-company">Brezarjev Mlin</p>
      <p class="contact-line">Tomaž Kralj s.p.</p>
      <p class="contact-line">Potok 18, 1296 Šentvid</p>
      <div class="contact-phones"><p class="contact-phone">T: 01 555 20 40</p><p class="contact-phone">M: 040 123 456</p></div>
      <p class="contact-web">www.brezarjev-mlin.si</p>
    </div>
  </section>

</main>
</body>
</html>
```